Revelation Sanctuary Flyer

We need a flyer for a church seminar that focuses on the Revelation and the sanctuary, it will show images with giants, UFOs maybe some pyramids, sanctuary furniture pieces.

Front Cover, Middle and Back cover. size 8.5 x 11 folded in the middle
The information is in file 1 and file 2.
The other files are examples and ideas for layout.

Target Market(s)

Churches

Requirements
Must have
• 1. Flyer design files have to be print ready.
• 2. Must have appropriate bleed size and safe zone
• PDF, JPEG, PSD, AI, TIFF
Nice to have
• Images of Giants, UFO, Sanctuary building, Pyramids

```html
<!DOCTYPE html>
<html lang="en">
<head>
<meta charset="utf-8">
<title>Sanctuary Seminar – Inside Spread</title>
<link href="https://fonts.googleapis.com/css2?family=Alfa+Slab+One&family=Arvo:wght@700&family=Lato:wght@400;700;900&display=swap" rel="stylesheet">
<style>
  :root{
    --purple:#2e1651;
    --purple-deep:#22103f;
    --gold:#c9bb5a;
    --title-gold:#e9c85a;
    --yellow:#f6ea1c;
    --cream:#f3e9a6;
    --ink:#111;
    --white:#fff;
  }
  *{margin:0;padding:0;box-sizing:border-box}
  html,body{width:1200px;height:1200px;overflow:hidden;background:var(--white)}
  body{position:relative;font-family:'Lato',sans-serif;color:var(--ink)}
  .label{position:absolute;font-family:'Lato',sans-serif;font-weight:400;color:var(--ink);white-space:nowrap;font-size:38px}
  .label-spread{left:468px;top:126px}
  .label-left{left:296px;top:168px}
  .label-right{left:812px;top:182px}

  .spread{position:absolute;left:90px;top:256px;width:1043px;height:805px;overflow:hidden}
  .spread-art{position:absolute;inset:0}

  .headline{position:absolute;left:0;width:1043px;top:14px;text-align:center;font-family:'Alfa Slab One',serif;font-size:42px;line-height:50px;
    background:linear-gradient(180deg,#fff3b0 0%,var(--title-gold) 45%,#b8862a 100%);-webkit-background-clip:text;background-clip:text;color:transparent;
    filter:drop-shadow(2px 3px 2px rgba(40,20,60,.55))}
  .subhead{position:absolute;left:0;width:1043px;top:66px;text-align:center;font-family:'Arvo',serif;font-weight:700;font-size:18px;color:#f3edd9;
    text-shadow:1px 1px 0 #3a2a55,-1px -1px 0 #3a2a55,1px -1px 0 #3a2a55,-1px 1px 0 #3a2a55}

  .speaker{position:absolute;left:24px;top:272px;width:222px;color:var(--white)}
  .speaker-kicker{font-family:'Arvo',serif;font-weight:700;font-size:13px;text-align:right;padding-right:2px}
  .speaker-name{font-family:'Arvo',serif;font-weight:700;font-size:24px;line-height:34px;margin-top:2px;white-space:nowrap;text-align:left}
  .speaker-bio{position:absolute;left:27px;width:218px;font-weight:700;font-size:12.4px;line-height:15.8px;color:var(--white)}
  .bio-1{top:352px}.bio-2{top:430px}.bio-3{top:526px}
  .invite{position:absolute;left:27px;top:612px;width:200px;font-weight:700;font-size:15px;line-height:19px;color:var(--yellow)}
  .features{position:absolute;left:27px;top:715px;list-style:none;font-family:'Arvo',serif;font-weight:700;font-size:15px;line-height:24px;color:var(--white)}
  .features li::before{content:"•";margin-right:10px;font-family:'Lato',sans-serif}

  .session{position:absolute;top:346px;width:247px;height:258px;background:var(--purple);text-align:center;color:var(--white)}
  .session-1{left:269px}.session-2{left:522px}.session-3{left:776px}
  .session-kind{margin-top:11px;font-size:15px;font-weight:700;letter-spacing:.2px}
  .session-title{font-family:'Arvo',serif;font-weight:700;font-size:20px;line-height:24px;color:var(--yellow)}
  .session-date{font-size:12.5px;font-weight:700;margin-top:1px}
  .session-art{position:absolute;left:10px;top:74px;width:227px;height:176px}
  .art-angels{background:linear-gradient(160deg,#8c925a,#545a2c 60%,#3c4020)}
  .art-pyramid{background:linear-gradient(180deg,#5c8b98 0%,#4a7683 55%,#37606d 100%)}
  .art-giant{background:radial-gradient(circle at 50% 35%,#c86a1c,#8a3a10 55%,#4a1a08)}

  .freebies{position:absolute;top:612px;left:0;width:1043px;font-family:'Arvo',serif;font-weight:700;font-size:15px;color:var(--purple)}
  .freebies span{position:absolute;white-space:nowrap}

  .topics{position:absolute;left:260px;top:652px;width:772px;height:148px;background:linear-gradient(90deg,#bfb254,#d6cb73 50%,#bfb254)}
  .topics-heading{position:absolute;left:20px;top:6px;font-family:'Arvo',serif;font-weight:700;font-size:23px;line-height:26px;color:var(--white);
    text-shadow:1px 1px 0 var(--purple),-1px -1px 0 var(--purple),1px -1px 0 var(--purple),-1px 1px 0 var(--purple)}
  .topics-table{position:absolute;left:114px;top:11px;width:632px;border-collapse:collapse;font-size:11.6px;font-weight:700}
  .topics-table td{height:18.4px;padding:0 0 0 13px;white-space:nowrap;color:var(--cream)}
  .topics-table tr.band td{background:var(--purple);color:var(--white)}
  .topics-table col.c1{width:159px}.topics-table col.c2{width:162px}.topics-table col.c3{width:160px}
</style>
</head>
<body>
  <div class="label label-spread">INSIDE SPREAD</div>
  <div class="label label-left">LEFT</div>
  <div class="label label-right">RIGHT</div>

  <section class="spread">
    <svg class="spread-art" width="1043" height="805" viewBox="0 0 1043 805">
      <defs>
        <linearGradient id="sky" x1="0" y1="0" x2="1" y2="0.6">
          <stop offset="0" stop-color="#8a7fa8"/>
          <stop offset="0.3" stop-color="#e9e3ee"/>
          <stop offset="0.65" stop-color="#b9aed0"/>
          <stop offset="1" stop-color="#4a3b6c"/>
        </linearGradient>
        <linearGradient id="panel" x1="0" y1="0" x2="1" y2="1">
          <stop offset="0" stop-color="#2e1651"/>
          <stop offset="0.6" stop-color="#3a2466"/>
          <stop offset="1" stop-color="#5a4f8c"/>
        </linearGradient>
        <linearGradient id="interior" x1="0" y1="0" x2="1" y2="1">
          <stop offset="0" stop-color="#f0a020"/>
          <stop offset="0.5" stop-color="#e8c66a"/>
          <stop offset="1" stop-color="#b65a14"/>
        </linearGradient>
        <linearGradient id="camp" x1="0" y1="0" x2="0" y2="1">
          <stop offset="0" stop-color="#c48a5c"/>
          <stop offset="0.4" stop-color="#e6d7c0"/>
          <stop offset="1" stop-color="#c9b89a"/>
        </linearGradient>
        <clipPath id="arc">
          <path d="M200,185 Q560,80 1043,100 L1043,805 L200,805 Z"/>
        </clipPath>
      </defs>
      <rect width="1043" height="805" fill="url(#sky)"/>
      <path d="M0,297 Q450,110 1043,133 L1043,805 L0,805 Z" fill="url(#panel)"/>
      <g clip-path="url(#arc)">
        <rect x="264" y="60" width="380" height="276" fill="url(#interior)" role="img" aria-label="Illustration of the holy place inside the sanctuary with lampstand, altar of incense and priest"/>
        <rect x="652" y="60" width="382" height="276" fill="url(#camp)" role="img" aria-label="Illustration of the wilderness tabernacle courtyard with tents and mountain behind"/>
      </g>
      <rect x="260" y="334" width="776" height="304" fill="#cfc468"/>
      <rect x="260" y="334" width="776" height="10" fill="#d9cd60" opacity=".7"/>
    </svg>

    <h1 class="headline">GOD’s Way is in The Sanctuary</h1>
    <p class="subhead">The Bible Provides Solid Answers To All Your Questions</p>

    <div class="speaker">
      <p class="speaker-kicker">Meet Our Speaker</p>
      <h2 class="speaker-name">Daniel Whitmore</h2>
    </div>
    <p class="speaker-bio bio-1">Daniel Whitmore presents Daniel and Revelation with simple wisdom, understanding and vivid illustrations that all ages can comprehend.</p>
    <p class="speaker-bio bio-2">He believes by knowing the events outlined in God's word, will prepare people to stand in the last days, and help them avoid the pitfalls that Satan has laid for mankind.</p>
    <p class="speaker-bio bio-3">Prophecy lets us know where we came from and where we are going. So come out and hear God's final message to the last generation.</p>
    <p class="invite">We invite you to bring the whole family and discover how Bible prophecy is relevant to our times.</p>
    <ul class="features">
      <li>Inspirational Singing</li>
      <li>Nightly Quizzes</li>
      <li>Health Topics</li>
    </ul>

    <article class="session session-1">
      <p class="session-kind">OPENING DAY!</p>
      <h3 class="session-title">Intro to Revelation!</h3>
      <p class="session-date">Saturday, May 19th - 11:00am</p>
      <div class="session-art art-angels" role="img" aria-label="Engraving of John receiving the vision of Revelation with angels"></div>
    </article>
    <article class="session session-2">
      <p class="session-kind">NIGHT SESSION</p>
      <h3 class="session-title">Ooparts!</h3>
      <p class="session-date">Saturday, May 19th - 7:00pm</p>
      <div class="session-art art-pyramid" role="img" aria-label="Photo of a great stone pyramid"></div>
    </article>
    <article class="session session-3">
      <p class="session-kind">SUNDAY SESSION</p>
      <h3 class="session-title">The Giants!</h3>
      <p class="session-date">Sunday, Juny 30th - 7:00pm</p>
      <div class="session-art art-giant" role="img" aria-label="Illustration of a giant towering over people"></div>
    </article>

    <div class="freebies">
      <span style="left:286px">FREE Admission</span>
      <span style="left:461px">FREE Study Guides</span>
      <span style="left:667px">FREE Books</span>
      <span style="left:832px">FREE Health Materials</span>
    </div>

    <section class="topics">
      <h2 class="topics-heading">Future<br>Topics</h2>
      <table class="topics-table">
        <colgroup><col class="c1"><col class="c2"><col class="c3"><col></colgroup>
        <tr class="band"><td>Chariots of the Gods</td><td>Mon. May 21 - 7:00 p.m.</td><td>Final Deception</td><td>Sun. May 27 - 7:00 p.m.</td></tr>
        <tr><td>The Great Disappointment</td><td>Tues. May 22 - 7:00 p.m.</td><td>Mark of the Beast &amp;</td><td>Mon. May 28 - 7:00 p.m.</td></tr>
        <tr class="band"><td>Sanctuary Furniture</td><td>Wed. May 23 - 7:00 p.m.</td><td>The 7 Last Plagues</td><td></td></tr>
        <tr><td>Israel, Evangelic &amp;</td><td>Fri. May 25 - 7:00 p.m.</td><td>The Woman in Red</td><td>Tues. May 29 - 7:00 p.m.</td></tr>
        <tr class="band"><td>Sanctuary Rebuilding</td><td></td><td>Crying Loud In the Rain</td><td>Wed. May 30 - 7:00 p.m.</td></tr>
        <tr><td>Futurism</td><td>Sat. May 26 - 11:00 a.m.</td><td>The Millennium</td><td>Fri.&nbsp; June 1 - 7:00 p.m.</td></tr>
        <tr class="band"><td>Summary</td><td>Sat. May 26 - 7:00 p.m.</td><td>The New Jerusalem</td><td>Sat.&nbsp; June 2 - 11:00 a.m.</td></tr>
      </table>
    </section>
  </section>
</body>
</html>
```